I need a creative wine label design for my brand called BIM BAM. A design that catches the eye of the millennial consumer! Something very creative and playing off of the BIM BAM concept.

This will be a Red Blend 2019 vintage from California

Target Market(s)

Millennial wine consumer

Requirements
Must have
• Must have a design that attracts the millennial wine consumer. This must have creative flare.
Should not have
• Nothing corny!

```html
<!DOCTYPE html>
<html lang="en">
<head>
<meta charset="utf-8">
<title>BIM BAM – Red Blend Label Range</title>
<link rel="stylesheet" href="https://fonts.googleapis.com/css2?family=Cormorant+Garamond:wght@500;600&display=swap">
<style>
  :root {
    --bg: #ffffff;
    --ink-soft: #5a5a5a;
    --gold: #b7891c;
    --gold-wash: #ece3b8;
    --rose: #ae1657;
    --rose-wash: #f2c9d6;
    --teal: #1f8a9e;
    --teal-wash: #cde2ea;
  }
  * { margin: 0; padding: 0; box-sizing: border-box; }
  html, body { width: 1200px; height: 800px; overflow: hidden; background: var(--bg); }
  body { font-family: "Cormorant Garamond", Georgia, serif; }

  .label-range {
    width: 1200px; height: 800px;
    display: flex; justify-content: center; align-items: center; gap: 70px;
  }

  .label {
    position: relative;
    width: 300px; height: 430px;
    --accent: var(--gold);
    --wash: var(--gold-wash);
  }
  .label--rose { --accent: var(--rose); --wash: var(--rose-wash); }
  .label--teal { --accent: var(--teal); --wash: var(--teal-wash); }

  .label__paper, .label__wash { position: absolute; inset: 0; width: 100%; height: 100%; }
  .label__paper .paper-fill { fill: url(#paperGradient); }
  .label__wash path { fill: var(--wash); opacity: .8; }

  .label__sprig {
    position: absolute; left: 150px; top: 290px;
    width: 130px; height: 120px;
    background: radial-gradient(ellipse at 50% 55%, var(--accent) 0%, transparent 68%);
    opacity: .4;
  }

  .label__brand {
    position: absolute; left: 0; right: 0; top: 170px;
    text-align: center;
    font-weight: 600; font-size: 74px; line-height: 1;
    color: var(--accent);
  }
  .label__type {
    position: absolute; left: 0; right: 0; top: 262px;
    text-align: center;
    font-weight: 600; font-size: 14px; letter-spacing: 1.5px; line-height: 1;
    color: var(--accent);
  }
  .label__abv {
    position: absolute; left: 22px; top: 288px;
    font-weight: 500; font-size: 14px; line-height: 1;
    color: var(--ink-soft);
  }
</style>
</head>
<body>
<svg width="0" height="0" style="position:absolute" aria-hidden="true">
  <defs>
    <linearGradient id="paperGradient" x1="0" y1="0" x2="1" y2="0">
      <stop offset="0" stop-color="#e6e6e7"/>
      <stop offset="0.35" stop-color="#fbfbfb"/>
      <stop offset="0.7" stop-color="#f6f6f6"/>
      <stop offset="1" stop-color="#e3e3e4"/>
    </linearGradient>
  </defs>
</svg>

<main class="label-range">
  <section class="label label--gold">
    <svg class="label__paper" viewBox="0 0 300 430" aria-hidden="true">
      <path class="paper-fill" d="M0,22 C40,8 70,30 105,14 C140,0 180,26 215,12 C255,2 280,20 300,10 L300,410 C270,422 235,400 195,414 C160,426 120,404 85,418 C50,428 20,410 0,420 Z"/>
    </svg>
    <svg class="label__wash" viewBox="0 0 300 430" role="img" aria-label="Soft golden watercolour wash">
      <path d="M0,350 C60,320 110,300 170,268 C220,240 270,226 300,214 L300,410 C270,422 235,400 195,414 C160,426 120,404 85,418 C50,428 20,410 0,420 Z"/>
    </svg>
    <div class="label__sprig" role="img" aria-label="Gold botanical sprig illustration"></div>
    <h2 class="label__brand">bim bam</h2>
    <p class="label__type">RED BLEND · CALIFORNIA</p>
    <p class="label__abv">2019 · 15%vol</p>
  </section>

  <section class="label label--rose">
    <svg class="label__paper" viewBox="0 0 300 430" aria-hidden="true">
      <path class="paper-fill" d="M0,22 C40,8 70,30 105,14 C140,0 180,26 215,12 C255,2 280,20 300,10 L300,410 C270,422 235,400 195,414 C160,426 120,404 85,418 C50,428 20,410 0,420 Z"/>
    </svg>
    <svg class="label__wash" viewBox="0 0 300 430" role="img" aria-label="Soft pink watercolour wash">
      <path d="M0,350 C60,320 110,300 170,268 C220,240 270,226 300,214 L300,410 C270,422 235,400 195,414 C160,426 120,404 85,418 C50,428 20,410 0,420 Z"/>
    </svg>
    <div class="label__sprig" role="img" aria-label="Magenta botanical sprig illustration"></div>
    <h2 class="label__brand">bim bam</h2>
    <p class="label__type">RED BLEND · CALIFORNIA</p>
    <p class="label__abv">2019 · 15%vol</p>
  </section>

  <section class="label label--teal">
    <svg class="label__paper" viewBox="0 0 300 430" aria-hidden="true">
      <path class="paper-fill" d="M0,22 C40,8 70,30 105,14 C140,0 180,26 215,12 C255,2 280,20 300,10 L300,410 C270,422 235,400 195,414 C160,426 120,404 85,418 C50,428 20,410 0,420 Z"/>
    </svg>
    <svg class="label__wash" viewBox="0 0 300 430" role="img" aria-label="Soft blue watercolour wash">
      <path d="M0,350 C60,320 110,300 170,268 C220,240 270,226 300,214 L300,410 C270,422 235,400 195,414 C160,426 120,404 85,418 C50,428 20,410 0,420 Z"/>
    </svg>
    <div class="label__sprig" role="img" aria-label="Teal botanical sprig illustration"></div>
    <h2 class="label__brand">bim bam</h2>
    <p class="label__type">RED BLEND · CALIFORNIA</p>
    <p class="label__abv">2019 · 15%vol</p>
  </section>
</main>
</body>
</html>
```